Print & digital package needed for technology firm

We need a package of coordinating marketing materials for our technology business. We offer technology solutions to midsized organizations, including data center, outsourced IT, and technology consulting. Find more information on our website, www.brightloomtech.com. Design is the main concern, we can modify the text ongoing to best reflect our company’s offerings. The design should communicate technology expertise and strategic thinking. Our website is currently being updated with a “flat design” theme and we’d like design of these items to be flat, fresh, modern, and professional, without being boring.
Please use attached logo - can send in .ai/.eps/.psd/etc. Fonts in logo are Futura, Futura Book, and Lato. Please use BRIGHTLOOM blue, #0372bb.
Please find attached one of our product flyers for one of the computers we lease. Fonts used are Roboto Slab (partial to this font) & Lato. Also attached copy of our business card design.
Taglines we have used include “Does IT hear your concerns?” and “IT made simple” although we are open to new ideas.
Would like final products to be available in editable files - .psd/.tif/.ai/etc.

- 1 PowerPoint template
- 1 leaderboard ad (digital, 72dpi)
- 1 medium rectangle ad 300x250 (digital, 72dpi)
- 1 full page ad 8x11 (print, 300dpi)
- 1 half-page ad horizontal (print, 300dpi)
- 1 letterhead template
- 1 proposal front-page

There is potential for further graphic/print design opportunities for our business as well.

All, thank you for your assistance in understanding the budget process with this type of design contest - we have updated the project's budget to reflect the items we are requesting.

Please email mvarela at brightloomtech.com with inquiries or comments. Thank you.

Designers,

Due to an oversight, our project was listed as "refundable" - this has been corrected and changed to committed payment.
To enter into this contest, please pick 2-3 items from the list of desired materials (ads, powerpoint, letterhead, etc.) It is not necessary to submit all items which will be part of the final package to be considered for the contest.

Thank you. Please contact mvarela@brightloomtech.com for questions.
Best,
Nell

CEOs, CFOs, CIOs, COOs - college+ educated, 30-60, professional.

Marketing

```html
<!DOCTYPE html>
<html lang="en">
<head>
<meta charset="utf-8">
<title>Brightloom – PowerPoint Template</title>
<link rel="stylesheet" href="https://fonts.googleapis.com/css2?family=Jost:wght@400;500;700&family=Lato:wght@400;700&display=swap">
<style>
  :root {
    --brand-blue: #0372bb;
    --deep-blue: #061598;
    --mid-blue: #0d74bb;
    --ink: #1a1a1a;
    --heading-blue: #0a6ab8;
    --paper: #ffffff;
  }
  * { margin: 0; padding: 0; box-sizing: border-box; }
  html, body { width: 1200px; height: 1000px; overflow: hidden; background: var(--paper); }
  body { position: relative; font-family: "Lato", sans-serif; color: var(--ink); }

  .board-title {
    position: absolute; left: 50px; top: 56px;
    font-family: "Jost", sans-serif; font-weight: 700;
    font-size: 22px; letter-spacing: 0.2px; color: var(--heading-blue);
  }

  .slide {
    position: absolute; width: 369px; height: 277px;
    background: var(--paper);
    box-shadow: 0 1px 6px rgba(0,0,0,0.35);
    overflow: hidden;
  }
  .slide .backdrop { position: absolute; inset: 0; width: 100%; height: 100%; }

  .col-1 { left: 30px; } .col-2 { left: 418px; } .col-3 { left: 807px; }
  .row-1 { top: 214px; } .row-2 { top: 507px; }

  .brand { position: absolute; right: 19px; top: 20px; text-align: right; }
  .brand-name {
    font-family: "Jost", sans-serif; font-weight: 500;
    font-size: 14px; line-height: 1; letter-spacing: 0.6px; color: var(--brand-blue);
  }
  .brand-url { font-size: 4.5px; font-weight: 700; color: var(--ink); margin-top: 3px; }

  .slide-footer {
    position: absolute; right: 19px; bottom: 16px; text-align: right; line-height: 1.5;
  }
  .footer-tagline { font-size: 6px; font-weight: 700; color: var(--brand-blue); }
  .footer-services { font-size: 6px; color: var(--ink); }

  .cover-title { position: absolute; left: 59px; top: 116px; color: var(--paper); }
  .cover-title h1 {
    font-family: "Jost", sans-serif; font-weight: 700; font-size: 21px; line-height: 1.1;
  }
  .cover-title p {
    font-family: "Jost", sans-serif; font-weight: 400; font-size: 15px; margin-top: 4px;
  }
</style>
</head>
<body>

<h2 class="board-title">POWER POINT TEMPLATE</h2>

<!-- Title slide -->
<section class="slide col-1 row-1">
  <svg class="backdrop" viewBox="0 0 369 277" aria-hidden="true">
    <polygon points="0,22 220,22 250,60 369,60 369,228 0,228" fill="var(--deep-blue)"/>
    <rect x="0" y="232" width="200" height="4" fill="var(--mid-blue)"/>
  </svg>
  <div class="brand"><div class="brand-name">BRIGHTLOOM</div><div class="brand-url">www.brightloomtech.com</div></div>
  <div class="cover-title"><h1>POWER POINT TEMPLATE</h1><p>POWER POINT TEMPLATE</p></div>
  <div class="slide-footer"><div class="footer-tagline">Technology Consultants &amp; Network Engineers</div><div class="footer-services">IT Consulting | Managed Services | Data Center</div></div>
</section>

<!-- Side-bar slide -->
<section class="slide col-2 row-1">
  <svg class="backdrop" viewBox="0 0 369 277" aria-hidden="true">
    <rect x="0" y="0" width="42" height="277" fill="var(--deep-blue)"/>
    <rect x="42" y="0" width="8" height="277" fill="var(--mid-blue)"/>
  </svg>
  <div class="brand"><div class="brand-name">BRIGHTLOOM</div><div class="brand-url">www.brightloomtech.com</div></div>
  <div class="slide-footer"><div class="footer-tagline">Technology Consultants &amp; Network Engineers</div><div class="footer-services">IT Consulting | Managed Services | Data Center</div></div>
</section>

<!-- Line slide -->
<section class="slide col-3 row-1">
  <svg class="backdrop" viewBox="0 0 369 277" aria-hidden="true">
    <line x1="0" y1="58" x2="369" y2="58" stroke="var(--brand-blue)" stroke-width="1.5"/>
  </svg>
  <div class="brand"><div class="brand-name">BRIGHTLOOM</div><div class="brand-url">www.brightloomtech.com</div></div>
  <div class="slide-footer"><div class="footer-tagline">Technology Consultants &amp; Network Engineers</div><div class="footer-services">IT Consulting | Managed Services | Data Center</div></div>
</section>

<!-- Header band slide -->
<section class="slide col-1 row-2">
  <svg class="backdrop" viewBox="0 0 369 277" aria-hidden="true">
    <rect x="0" y="0" width="230" height="40" fill="var(--deep-blue)"/>
    <rect x="0" y="40" width="230" height="6" fill="var(--mid-blue)"/>
  </svg>
  <div class="brand"><div class="brand-name">BRIGHTLOOM</div><div class="brand-url">www.brightloomtech.com</div></div>
  <div class="slide-footer"><div class="footer-tagline">Technology Consultants &amp; Network Engineers</div><div class="footer-services">IT Consulting | Managed Services | Data Center</div></div>
</section>

<!-- Frame lines slide -->
<section class="slide col-2 row-2">
  <svg class="backdrop" viewBox="0 0 369 277" aria-hidden="true">
    <line x1="0" y1="58" x2="369" y2="58" stroke="var(--deep-blue)" stroke-width="1.5"/>
    <line x1="0" y1="232" x2="369" y2="232" stroke="var(--deep-blue)" stroke-width="1.5"/>
  </svg>
  <div class="brand"><div class="brand-name">BRIGHTLOOM</div><div class="brand-url">www.brightloomtech.com</div></div>
  <div class="slide-footer"><div class="footer-tagline">Technology Consultants &amp; Network Engineers</div><div class="footer-services">IT Consulting | Managed Services | Data Center</div></div>
</section>

<!-- Filled frame slide -->
<section class="slide col-3 row-2">
  <svg class="backdrop" viewBox="0 0 369 277" aria-hidden="true">
    <rect x="0" y="58" width="369" height="174" fill="var(--mid-blue)"/>
  </svg>
  <div class="brand"><div class="brand-name">BRIGHTLOOM</div><div class="brand-url">www.brightloomtech.com</div></div>
  <div class="slide-footer"><div class="footer-tagline">Technology Consultants &amp; Network Engineers</div><div class="footer-services">IT Consulting | Managed Services | Data Center</div></div>
</section>

</body>
</html>
```